Web app UI design

This web app has been built and the UI needs a refresh.

Attached are the pages which need the refresh.

The web app is for a cyber security product/service and customers are inputting their details.

```html
<!DOCTYPE html>
<html lang="en">
<head>
<meta charset="utf-8">
<title>Profile info</title>
<link href="https://fonts.googleapis.com/css2?family=Roboto:wght@400;500;700&display=swap" rel="stylesheet">
<style>
  :root{
    --sidebar:#2e3243;
    --sidebar-top:#272a37;
    --sidebar-text:#ffffff;
    --sidebar-muted:#b9bcc8;
    --page-bg:#f0f1f5;
    --white:#ffffff;
    --ink:#222222;
    --label:#555a63;
    --field:#f1f2f5;
    --placeholder:#9a9ea6;
    --blue:#3b8cf0;
    --button:#4b93f3;
    --online:#3ccf4e;
    --rule:#e6e7eb;
  }
  *{box-sizing:border-box;margin:0;padding:0}
  html,body{width:1200px;height:818px;overflow:hidden}
  body{font-family:"Roboto",sans-serif;background:var(--page-bg);position:relative;color:var(--ink)}

  .sidebar{position:absolute;left:0;top:0;width:217px;height:818px;background:var(--sidebar);color:var(--sidebar-text)}
  .brand{height:70px;background:var(--sidebar-top);display:flex;align-items:center;padding-left:44px;gap:12px}
  .brand-mark{width:20px;height:20px;border-radius:50%;background:var(--white)}
  .brand-name{font-size:17px;letter-spacing:5px;font-weight:400}
  .avatar{position:absolute;left:50px;top:125px;width:116px;height:116px;border-radius:50%;
    background:linear-gradient(135deg,#5e8fb8 0%,#9cc3d6 45%,#c9b08a 75%,#2a2a2a 100%)}
  .status-dot{position:absolute;left:133px;top:225px;width:15px;height:15px;border-radius:50%;background:var(--online);border:2px solid var(--white)}
  .user-name{position:absolute;left:0;width:217px;top:258px;text-align:center;font-size:15px}
  .user-status{position:absolute;left:0;width:217px;top:279px;text-align:center;font-size:10px;color:var(--sidebar-muted)}
  .user-link{position:absolute;left:0;width:217px;top:297px;text-align:center;font-size:10px;color:var(--blue);text-decoration:underline}
  .nav{position:absolute;left:28px;top:369px;list-style:none}
  .nav li{display:flex;align-items:center;height:42px;gap:14px;font-size:13.5px}
  .nav svg{width:17px;height:17px;fill:#e9eaee}
  .sidebar-foot{position:absolute;left:0;width:217px;top:793px;text-align:center;font-size:9.5px;color:var(--sidebar-muted)}

  .topbar{position:absolute;left:217px;top:0;right:0;height:75px;background:var(--white)}
  .menu-btn{position:absolute;left:26px;top:17px;width:40px;height:40px;border-radius:50%;background:#eef0f3;display:flex;align-items:center;justify-content:center}
  .logout{position:absolute;right:27px;top:29px;display:flex;align-items:center;gap:7px;font-size:14px}
  .page-head{position:absolute;left:217px;top:82px;right:0;height:100px;background:var(--white)}
  .page-title{position:absolute;left:34px;top:34px;display:flex;align-items:center;gap:15px;font-size:23px;font-weight:400}
  .help{position:absolute;right:35px;top:40px;display:flex;align-items:center;gap:6px;color:var(--blue);font-size:14px}

  .card{position:absolute;left:243px;top:232px;width:925px;height:483px;background:var(--white);border-radius:3px}
  .notice{position:absolute;left:42px;top:41px;font-size:15px;color:#333}
  .notice b{font-weight:500;color:#111}
  .rule{position:absolute;left:38px;top:76px;width:850px;height:1px;background:var(--rule)}
  .field-label{position:absolute;font-size:13.3px;line-height:16px;color:var(--label);display:flex;align-items:center;gap:8px}
  .field{position:absolute;width:322px;height:38px;background:var(--field);border-radius:2px;padding-left:14px;display:flex;align-items:center;font-size:11.7px;color:#444}
  .field.empty{color:var(--placeholder)}
  .cancel{position:absolute;left:674px;top:416px;font-size:13.5px;color:var(--blue);font-weight:500}
  .save{position:absolute;left:749px;top:399px;width:135px;height:50px;background:var(--button);color:var(--white);border-radius:2px;display:flex;align-items:center;justify-content:center;font-size:13.5px;font-weight:500}
  .main-foot{position:absolute;left:258px;top:793px;font-size:9.5px;color:#555}
</style>
</head>
<body>
  <aside class="sidebar">
    <div class="brand"><span class="brand-mark"></span><span class="brand-name">SECURA</span></div>
    <div class="avatar" role="img" aria-label="User profile photo"></div>
    <span class="status-dot"></span>
    <div class="user-name">User’s Name</div>
    <div class="user-status">Online</div>
    <div class="user-link">View profile</div>
    <ul class="nav">
      <li><svg viewBox="0 0 24 24"><path d="M12 3 3 10v11h6v-6h6v6h6V10z"/></svg>Home</li>
      <li><svg viewBox="0 0 24 24"><path d="M2 3h3l1 3h16l-3 8H8l-1 2h13v2H4l3-5L4 5H2z"/><circle cx="8" cy="21" r="1.6"/><circle cx="18" cy="21" r="1.6"/></svg>Subscriptions</li>
      <li><svg viewBox="0 0 24 24"><path d="M6 10V7a6 6 0 0 1 12 0v3h1v12H5V10zm2.5 0h7V7a3.5 3.5 0 0 0-7 0z"/></svg>Verify</li>
      <li><svg viewBox="0 0 24 24"><path d="M12 2 21 7v10l-9 5-9-5V7zm0 7a3 3 0 1 0 0 6 3 3 0 0 0 0-6z"/></svg>Settings</li>
    </ul>
    <div class="sidebar-foot">Privacy policy &nbsp;|&nbsp; Contact us</div>
  </aside>

  <header class="topbar">
    <div class="menu-btn"><svg width="16" height="13" viewBox="0 0 16 13"><path d="M0 1h16M0 6.5h16M0 12h16" stroke="#222" stroke-width="1.6"/></svg></div>
    <div class="logout"><svg width="14" height="14" viewBox="0 0 14 14"><rect width="14" height="14" fill="#111"/><path d="M3 7h6M7 4l3 3-3 3" stroke="#fff" stroke-width="1.6" fill="none"/></svg>Log out</div>
  </header>

  <section class="page-head">
    <h1 class="page-title"><svg width="28" height="31" viewBox="0 0 28 31" fill="none" stroke="#222" stroke-width="1.2"><rect x="1" y="5" width="18" height="25" rx="1"/><rect x="6" y="1" width="21" height="25" rx="1" fill="#fff"/><circle cx="16" cy="9" r="3"/><path d="M11 18c0-4 10-4 10 0M10 21h12M10 23.5h12"/></svg>Profile info</h1>
    <div class="help">Need help <svg width="17" height="17" viewBox="0 0 17 17"><circle cx="8.5" cy="8.5" r="7.5" fill="none" stroke="#3b8cf0" stroke-width="1.5"/><text x="8.5" y="12.3" text-anchor="middle" font-size="10.5" font-family="Roboto,sans-serif" fill="#3b8cf0">?</text></svg></div>
  </section>

  <main class="card">
    <p class="notice">Only your <b>company name</b>, <b>ACN</b> and <b>ABN</b> from below will be shared on your profile</p>
    <div class="rule"></div>

    <label class="field-label" style="left:54px;top:123px">Email (Cannot be changed)</label>
    <div class="field empty" style="left:49.5px;top:146px">Enter email here...</div>
    <label class="field-label" style="left:396px;top:123px">Company Legal Name</label>
    <div class="field empty" style="left:395px;top:146px">Enter company name here...</div>

    <label class="field-label" style="left:54px;top:209px">ACN <svg width="14" height="14" viewBox="0 0 14 14"><circle cx="7" cy="7" r="6.2" fill="none" stroke="#3b8cf0" stroke-width="1.3"/><text x="7" y="10.2" text-anchor="middle" font-size="9" font-family="Roboto,sans-serif" fill="#3b8cf0">?</text></svg></label>
    <div class="field" style="left:49.5px;top:231px">111111</div>
    <label class="field-label" style="left:399px;top:209px">ABN <svg width="14" height="14" viewBox="0 0 14 14"><circle cx="7" cy="7" r="6.2" fill="none" stroke="#3b8cf0" stroke-width="1.3"/><text x="7" y="10.2" text-anchor="middle" font-size="9" font-family="Roboto,sans-serif" fill="#3b8cf0">?</text></svg></label>
    <div class="field" style="left:395px;top:231px">222222</div>

    <label class="field-label" style="left:54px;top:293px">Contact Number</label>
    <div class="field" style="left:49.5px;top:315.5px">000 000 0000</div>

    <span class="cancel">Cancel</span>
    <span class="save">Save profile</span>
  </main>

  <footer class="main-foot">Secura Me @ 2023</footer>
</body>
</html>
```